Elegant and modern body scrub for organic junkies

I need a package design for my new company based out of Austin, Texas. We are focused on cruelty free and all natural and organic products. Our deign needs to be able to have the information we require on it, while still appearing very clean and captivating. Our initial product is a clear skin body scrub, intended for people with problematic skin. Our target market is women and we want to show elegance, without appearing "high end."
Updates

Reason: I want to allot more time for certain designers to submit edits. Last minute proposals have been appealing

Target Market(s)

Women. Organic and holistic minded. Natural beauty lovers.

Industry/Entity Type

Skin Care Product

Font styles to use
Script
Other font styles liked:
• AmericanTypewriter, Beautifulflaws, courier, caviarDreams-bold

Colors
000000
ffc214
ffffff
fece3e
fbee3e

Requirements
Must have
• Must be designed in Adobe Illustrator.
• The photo titled “structure for oz and grams” -That needs to be included at the bottom of 1B. I like the horizontal and vertical bar that separate the two. I want that.
• Color Inspiration - The photo titled “venra color inspiration” and “color combo inspiration” are the colors I want. BLACK, GOLD, WHITE. I want the label background black and the writing in white with some gold somewhere on it. My logo is going to be a Saffron Grove.
• The photos titled “I like how clean this looks” and “I also like how clean this looks” - I want 1B to look super clean. I don’t want a lot of information in this box. I want simple and clean. This is where the logo and brand name will go.
• Logo - A Saffron Grove. I want it to be gold and geometric. There can be dimension like this elephant example on the left of the 1B description. I want the trunk to be facing to the left and the trunk needs to be raised overhead and touching the animal's forehead.
• The photo titled “sideways writing and silver rim” - I want 1C to be written sideways like this. My text will be much more extensive so the font won’t be able to be so big.
Nice to have
• The photo titled “sideways writing and silver rim” - I want 1C to be written sideways like this. My text will be much more extensive so the font won’t be able to be so big. I also REALLY like how this label is rimmed in silver, but I would want gold. This is not mandatory, but I really like this.
• The photo titled “melted honey” - This is another option I really like. The gold that looks like honey dripping on the label is really cool. Not mandatory, but I really liked that. I also like the craft background on this.
• Color Inspiration - The photo titled “color inspiration” and “another color inspiration” is an option I would also like to see. Rather than black, I’d like to see what it would ALSO look like with a navy background. NAVY, GOLD, WHITE, maybe black somewhere.
Should not have
• Colorful patterns or excessive info in section 1B.

```html
<!DOCTYPE html>
<html lang="en">
<head>
<meta charset="utf-8">
<title>Saffron Grove body scrub label</title>
<link href="https://fonts.googleapis.com/css2?family=Courier+Prime:wght@400;700&family=Quicksand:wght@400&display=swap" rel="stylesheet">
<style>
  :root {
    --backdrop: #e9e9e9;
    --label: #000000;
    --ink: #ffffff;
    --gold: #ffc214;
    --gold-soft: #fece3e;
    --art-dark: #1c1606;
  }
  html, body {
    margin: 0;
    padding: 0;
    width: 1200px;
    height: 866px;
    overflow: hidden;
    background: var(--backdrop);
  }
  .stage {
    width: 1200px;
    height: 866px;
    display: flex;
    align-items: center;
    justify-content: center;
  }
  .label {
    width: 820px;
    height: 360px;
    background: var(--label);
    box-sizing: border-box;
    border: 3px solid var(--gold);
    outline: 1px solid var(--gold);
    outline-offset: -12px;
    padding: 44px 60px 44px 66px;
    display: flex;
    align-items: center;
    gap: 40px;
    box-shadow: 0 2px 10px rgba(0,0,0,0.12);
  }
  .emblem-art {
    width: 220px;
    height: 250px;
    flex: none;
    border-radius: 4px;
    background: linear-gradient(160deg, var(--gold-soft), #b88a10 70%, var(--art-dark));
  }
  .info {
    flex: 1;
    color: var(--ink);
    font-family: "Courier Prime", "Courier New", monospace;
    white-space: nowrap;
  }
  .brand-name {
    font-size: 27px;
    letter-spacing: 1px;
    padding: 0 0 10px 8px;
    border-bottom: 2px solid var(--gold);
    margin: 0;
    font-weight: 400;
    color: var(--gold);
  }
  .product-row {
    display: flex;
    border-bottom: 2px solid var(--gold);
  }
  .product-type, .product-year {
    font-size: 27px;
    padding: 14px 8px;
  }
  .product-type {
    border-right: 2px solid var(--gold);
    padding-right: 18px;
  }
  .product-year { padding-left: 24px; }
  .product-purpose {
    font-size: 30px;
    padding: 16px 8px 14px;
    border-bottom: 2px solid var(--gold);
    margin: 0;
  }
  .maker-note {
    font-family: "Quicksand", "Helvetica Neue", sans-serif;
    font-size: 18px;
    padding: 18px 8px 0;
    margin: 0;
  }
</style>
</head>
<body>
  <main class="stage">
    <section class="label">
      <svg class="emblem-art" role="img" aria-label="Geometric gold elephant illustration with raised trunk" viewBox="0 0 220 250"></svg>
      <div class="info">
        <h1 class="brand-name">SAFFRON GROVE</h1>
        <div class="product-row">
          <span class="product-type">body scrub</span>
          <span class="product-year">1989</span>
        </div>
        <p class="product-purpose">For problematic skin</p>
        <p class="maker-note">Handmade in small batches with Love</p>
      </div>
    </section>
  </main>
</body>
</html>
```